Website design for a Fine Food exhibition in Asia

We need a website design for a Food and Wine exhibition (home page). The name of the exhibition is "Savorix" which is going to be Held in south korea. The concept is "Fine Food" in major, qui means clustering Would not we accept Any canned food, fast food, chips, thesis kind of foods. We do not open to the public like Some Other Food exhibitions do, Then only trade visitors. The EXHIBITORS will come from all the World. The categories we Would like to make is in attachment below. We will update the text When the category's share will be done. We need a color can qui correspond well to the "Find Food ', color of our logo qui est in attachment Would be good. You can offer us some photos, images, like photos of fine food corners in supermarkets, gourmet shops like photos of etc. ... You can find links Some of "same" exhibitions in below, qui can give you a guideline of the kind of website we expect. http://en.plumbarrow-fairhall.com/ http://velmontrade.com/ http: //www.tarnicplaza. co.kr We will ask to the winning designer to Develop the full website under Wordpress.
Updates

Project Deadline Extended
Reason: Because we need some modifications to requests.

Target Market(s)

Fine food, gourmet food, "grocery", pastry, bakery

Number of Pages Required

5+ page

Font styles to use
Sans Serif

Colors
886aae
6b449b
e34197
e667a6
9bcb3c
f58947
f37122
ec1f27

Requirements
Must have
• Warm colors, and layout showing the high level of foods, fine foods, gourmet foods
Nice to have
• It would be nice to include the sentence "The new meeting place for the gourmet food in Asia"

```html
<!DOCTYPE html>
<html lang="en">
<head>
<meta charset="utf-8">
<title>Savorix – Exhibitors</title>
<link href="https://fonts.googleapis.com/css2?family=Roboto:wght@300;400;500;700&display=swap" rel="stylesheet">
<style>
:root{
  --plum:#5e0a5e;
  --plum-dark:#4a0749;
  --magenta:#d6006f;
  --white:#ffffff;
  --ink:#222222;
  --muted:#444444;
  --row-alt:#eeeeee;
  --photo-a:#c9cfd6;
  --photo-b:#7a8a99;
  --map-a:#ece8df;
  --map-b:#d7dccb;
}
*{margin:0;padding:0;box-sizing:border-box}
html,body{width:679px;height:1200px;overflow:hidden;background:var(--white)}
body{position:relative;font-family:'Roboto',sans-serif;color:var(--ink)}
.abs{position:absolute}

/* header */
.top-rule{left:0;top:0;width:679px;height:2px;background:var(--plum)}
.brand{left:112px;top:12px;display:flex;align-items:center;gap:6px}
.brand-mark{width:14px;height:14px;border-radius:50%;background:var(--plum)}
.brand-name{font-size:22px;font-weight:400;color:var(--plum);letter-spacing:.5px;line-height:1}
.brand-tag{left:113px;top:38px;font-size:8px;color:var(--magenta)}
.event-date{left:340px;top:2px;width:230px;height:51px;background:var(--magenta);clip-path:polygon(16% 0,100% 0,84% 100%,0 100%)}
.event-date .d{position:absolute;left:44px;top:11px;color:var(--white);font-size:13.5px;font-weight:500}
.event-date .p{position:absolute;left:44px;top:27px;color:var(--white);font-size:9px}

/* nav */
.main-nav{left:0;top:53px;width:679px;height:22px;background:var(--plum)}
.home{position:absolute;left:114px;top:3px;width:16px;height:16px;border-radius:50%;background:var(--magenta)}
.home svg{position:absolute;left:4px;top:3.5px}
.nav-link{position:absolute;top:7px;font-size:7.5px;font-weight:500;color:var(--white)}
.nav-link.active{color:var(--magenta)}

/* banner */
.banner{left:0;top:76px;width:679px;height:71px;background:var(--magenta)}
.banner-photo{position:absolute;left:336px;top:0;width:343px;height:71px;background:linear-gradient(90deg,var(--photo-a),var(--photo-b));clip-path:polygon(17% 0,100% 0,100% 100%,0 100%)}
.banner h1{position:absolute;left:117px;top:26px;font-size:18px;font-weight:700;color:var(--white);letter-spacing:.5px}

/* sidebar */
.sidebar{left:109px;top:177px;width:118px;height:273px;background:var(--plum)}
.side-link{display:block;height:20.5px;padding:7px 0 0 10px;font-size:7px;color:var(--white);border-bottom:1px solid var(--plum-dark)}
.side-accent{position:absolute;left:0;top:104px;width:118px;height:169px;background:var(--magenta);clip-path:polygon(100% 0,100% 100%,0 100%,0 88%)}
.side-seal{position:absolute;left:21px;top:126px;width:78px;height:78px;border-radius:50%;background:var(--white);border:3px solid var(--plum);display:flex;align-items:center;justify-content:center;font-size:13px;color:var(--plum)}
.side-date{position:absolute;left:0;width:118px;text-align:center;color:var(--white)}

/* content */
.section-title{left:246px;font-size:17.5px;font-weight:300;color:var(--plum)}
.copy{left:247px;width:320px;font-size:6.4px;line-height:11.2px;color:var(--ink);text-align:justify}
.content-photo{left:249px;top:292px;width:314px;height:104px;background:linear-gradient(100deg,var(--photo-b),var(--photo-a) 55%,var(--photo-b))}
.btn{left:247px;top:516px;width:97px;height:23px;background:var(--magenta);color:var(--white);font-size:10px;font-weight:700;text-align:center;line-height:23px}

.booth-table{left:247px;top:671px;width:319px;border:1px solid var(--plum);border-radius:3px;border-collapse:collapse;font-size:8px;overflow:hidden}
.booth-table th{background:var(--plum);color:var(--white);font-size:10px;font-weight:500;text-align:left;height:23px;padding-left:8px}
.booth-table td{height:22.5px;padding-left:8px}
.booth-table tr:nth-child(2) td{background:var(--row-alt)}
.booth-table .price{width:65px}

/* contact */
.contact{left:0;top:770px;width:679px;height:144px;background:var(--plum)}
.contact-map{position:absolute;left:250px;top:0;width:429px;height:144px;background:linear-gradient(135deg,var(--map-a),var(--map-b));clip-path:polygon(27% 0,100% 0,100% 100%,0 100%)}
.contact h2{position:absolute;left:114px;top:16px;font-size:17.5px;font-weight:300;color:var(--white)}
.contact p{position:absolute;left:115px;width:142px;font-size:6.6px;line-height:9px;color:var(--white);text-align:justify}
.pin{position:absolute;left:516px;top:55px}

/* partners */
.partners-title{left:0;top:942px;width:679px;text-align:center;font-size:17.5px;font-weight:300;color:var(--ink)}
.partner{position:absolute;top:983px;height:20px;border-radius:2px}

/* footer */
.footer{left:0;top:1034px;width:679px;height:118px;background:var(--magenta)}
.footer-seal{position:absolute;left:112px;top:19px;width:80px;height:80px;border-radius:50%;background:var(--white);border:3px solid var(--plum);display:flex;align-items:center;justify-content:center;font-size:13px;color:var(--plum)}
.footer-date{position:absolute;left:201px;color:var(--white)}
.newsletter{position:absolute;left:345px;top:0;width:225px;height:118px;background:var(--plum);clip-path:polygon(51% 0,100% 0,51% 100%,0 100%)}
.newsletter-title{position:absolute;left:425px;top:12px;font-size:17.5px;font-weight:300;color:var(--white)}
.email{position:absolute;left:426px;top:48px;width:90px;height:19px;background:var(--magenta);color:var(--white);font-size:7px;padding:6px 0 0 5px}
.submit{position:absolute;left:426px;top:76px;width:49px;height:19px;background:var(--magenta);color:var(--white);font-size:8px;font-weight:700;text-align:center;line-height:19px;border:1px solid var(--white)}

.legal{left:112px;top:1173px;font-size:6.5px;color:var(--ink)}
.foot-link{position:absolute;top:1173px;font-size:7.3px;font-weight:500;color:var(--magenta)}
</style>
</head>
<body>

<div class="abs top-rule"></div>

<header>
  <div class="abs brand"><span class="brand-mark"></span><span class="brand-name">Savorix</span></div>
  <div class="abs brand-tag">The Fine Food Event in Asia</div>
  <div class="abs event-date"><span class="d">02-03 NOV. 2017</span><span class="p">HALLVERA, SEOUL, SOUTH KOREA</span></div>
</header>

<nav class="abs main-nav">
  <span class="home"><svg width="8" height="8" viewBox="0 0 8 8"><path d="M4 0 L8 4 H7 V8 H5 V5.5 H3 V8 H1 V4 H0 Z" fill="#fff"/></svg></span>
  <span class="nav-link" style="left:259px">THE EXHIBITION</span>
  <span class="nav-link active" style="left:346px">EXHIBITORS</span>
  <span class="nav-link" style="left:418px">VISITORS</span>
  <span class="nav-link" style="left:481px">EVENTS</span>
  <span class="nav-link" style="left:538px">MEDIA</span>
</nav>

<section class="abs banner">
  <div class="banner-photo" role="img" aria-label="Photo of trade visitors walking through an exhibition hall"></div>
  <h1>EXHIBITORS</h1>
</section>

<aside class="abs sidebar">
  <a class="side-link">WHO ARE THE EXHIBITORS?</a>
  <a class="side-link">EXHIBITOR REGISTRATION</a>
  <a class="side-link">EXHIBITORS' LIST</a>
  <a class="side-link">BOOTH OPTIONS</a>
  <a class="side-link">CONTACT US</a>
  <div class="side-accent"></div>
  <div class="side-seal">Savorix</div>
  <div class="side-date" style="top:216px;font-size:9.5px;font-weight:500">02-03 NOV. 2017</div>
  <div class="side-date" style="top:232px;font-size:9px;line-height:10px">HALLVERA, SEOUL,<br>SOUTH KOREA</div>
</aside>

<h2 class="abs section-title" style="top:172px">WHO ARE THE EXHIBITORS?</h2>
<p class="abs copy" style="top:208px">Lorem Ipsum is simply dummy text of the printing and typesetting industry. Lorem Ipsum has been the industry's standard dummy text ever since the 1500s, when an unknown printer took a galley of type and scrambled it to make a type specimen book. It has survived not only five centuries, but also the leap into electronic typesetting, remaining essentially unchanged. It was popularised in the 1960s with the release of Letraset sheets containing Lorem Ipsum passages, and more recently with desktop publishing software like Aldus PageMaker including versions of Lorem Ipsum.</p>
<div class="abs content-photo" role="img" aria-label="Photo of exhibitors and visitors talking at a busy food fair"></div>

<h2 class="abs section-title" style="top:422px">EXHIBITOR REGISTRATION</h2>
<p class="abs copy" style="top:458px">Lorem Ipsum is simply dummy text of the printing and typesetting industry. Lorem Ipsum has been the industry's standard dummy text ever since the 1500s, when an unknown printer took a galley of type and scrambled it to make a type specimen book. It has survived not only five centuries, but also the leap into electronic typesetting, remaining essentially unchanged.</p>
<a class="abs btn">REGISTER NOW</a>

<h2 class="abs section-title" style="top:579px">BOOTH OPTIONS</h2>
<p class="abs copy" style="top:615px">Lorem Ipsum is simply dummy text of the printing and typesetting industry. Lorem Ipsum has been the industry's standard dummy text ever since the 1500s, when an unknown printer took a galley of type and scrambled it to make a type specimen book. It has survived not only five centuries, but also the leap into electronic typesetting, remaining essentially unchanged.</p>
<table class="abs booth-table">
  <tr><th>Booth Type</th><th class="price">Unit Price</th></tr>
  <tr><td>Standard Booth</td><td>$9999</td></tr>
  <tr><td>Premium Booth</td><td>$9999</td></tr>
</table>

<section class="abs contact">
  <div class="contact-map" role="img" aria-label="Street map of the exhibition venue area"></div>
  <svg class="pin" width="10" height="16" viewBox="0 0 10 16"><path d="M5 0 C2 0 0 2.2 0 5 C0 9 5 16 5 16 C5 16 10 9 10 5 C10 2.2 8 0 5 0 Z" fill="#d32f2f"/><circle cx="5" cy="5" r="1.8" fill="#7a1010"/></svg>
  <h2>CONTACT US</h2>
  <p style="top:52px">Lorem Ipsum is simply dummy text of the printing and typesetting industry.</p>
  <p style="top:79px">Lorem Ipsum has been the industry's standard dummy text ever since the 1500s, when an unknown printer took a galley of type and scrambled it to make a type specimen book.</p>
</section>

<h2 class="abs partners-title">PARTNERS</h2>
<div class="partner" style="left:112px;width:40px;background:#7a2a2a"></div>
<div class="partner" style="left:169px;width:43px;background:#b22a2a"></div>
<div class="partner" style="left:230px;width:40px;background:#2a6bb2"></div>
<div class="partner" style="left:286px;width:45px;background:#e0a020"></div>
<div class="partner" style="left:348px;width:41px;background:#333333"></div>
<div class="partner" style="left:402px;width:45px;background:#b0185a"></div>
<div class="partner" style="left:463px;width:42px;background:#c0281e"></div>
<div class="partner" style="left:520px;width:46px;background:#9bcb3c"></div>

<footer class="abs footer">
  <div class="footer-seal">Savorix</div>
  <div class="footer-date" style="top:42px;font-size:12px;font-weight:500">02-03 NOV. 2017</div>
  <div class="footer-date" style="top:61px;font-size:11px">HALLVERA, SEOUL, SOUTH KOREA</div>
  <div class="newsletter"></div>
  <div class="newsletter-title">NEWSLETTER</div>
  <div class="email">ENTER EMAIL ID</div>
  <div class="submit">SUBMIT</div>
</footer>

<div class="abs legal">Copyright © 2017 SAVORIX. All Rights Reserved.</div>
<span class="foot-link" style="left:324px">THE EXHIBITION</span>
<span class="foot-link" style="left:395px">EXHIBITORS</span>
<span class="foot-link" style="left:452px">VISITORS</span>
<span class="foot-link" style="left:499px">EVENTS</span>
<span class="foot-link" style="left:541px">MEDIA</span>

</body>
</html>
```